Stationary for Keeping Steady

we are in the process of creating a more professional image for our company Keeping Steady Paramedical Services. We have recently had a new logo and general brochure designed using artpitchhub and have been impressed by the quality of submissions.

We need:
- Letterhead (A4)
- Business Cards
- With compliments slips
- Email stationary

Letterhead information:
Address - 47 Wattlebrook Drive, Fernhollow Vic 3091
Phone - 1800 462 817
email - enquiries@keepsteady.com.au
Internet - www.keepsteady.com.au
ABN - 82 463 915 207
ACN - 264 871 035

Files need to be able to be edited in Illustrator CS2

Business Cards / with compliments slips / email stationary:
Double sided.
One side to have Name, Mobile number, company phone 1800462817, email, internet address

Files need to be able to be edited in Illustrator CS2 (except email stationary)

Our website is www.keepsteady.com.au for more information. Do not base designs on the website as it will eventually be revised.

Target Market(s)

Australian based businesses, government departments and schools. We specialise in corporate customers rather than public first aid course

Industry/Entity Type

Internet

Requirements
Must have
• Where applicable file to be editable in illustrator CS2 to allow future alterations.

```html
<!DOCTYPE html>
<html lang="en">
<head>
<meta charset="utf-8">
<title>Keeping Steady – Stationery Set</title>
<link href="https://fonts.googleapis.com/css2?family=Questrial&display=swap" rel="stylesheet">
<style>
  :root {
    --bg-light: #e9e9e9;
    --bg-dark: #bdbdbd;
    --paper: #ffffff;
    --brand-red: #c8262c;
    --ink: #1a1a1a;
    --on-dark: #ffffff;
    --shadow: rgba(0,0,0,0.45);
  }
  * { margin: 0; padding: 0; box-sizing: border-box; }
  html, body { width: 1047px; height: 1200px; overflow: hidden; }
  body {
    position: relative;
    font-family: "Questrial", "Century Gothic", sans-serif;
    background: linear-gradient(90deg, var(--bg-light) 0%, #d6d6d6 55%, var(--bg-dark) 100%);
    color: var(--ink);
  }
  .sheet { position: absolute; background: var(--paper); box-shadow: 4px 6px 10px var(--shadow); overflow: hidden; }
  .sheet svg.swoosh { position: absolute; inset: 0; width: 100%; height: 100%; }

  /* wordmark: invented name, one colour, one weight, plain square beside */
  .wordmark { position: absolute; display: flex; align-items: center; gap: 14px; color: var(--brand-red); white-space: nowrap; }
  .wordmark .mark-square { background: var(--brand-red); flex: none; }
  .wordmark .name, .wordmark .sub { display: block; line-height: 1.05; }
  .wordmark.on-dark { color: var(--on-dark); }
  .wordmark.on-dark .mark-square { background: var(--on-dark); }

  /* letterhead */
  .letterhead { left: 208px; top: 35px; width: 800px; height: 1133px; z-index: 1; }
  .letterhead .wordmark { left: 24px; top: 26px; }
  .letterhead .mark-square { width: 96px; height: 96px; }
  .letterhead .name { font-size: 44px; }
  .letterhead .sub { font-size: 20px; }
  .letterhead .footer {
    position: absolute; right: 33px; bottom: 28px; text-align: right;
    color: var(--on-dark); font-size: 11.5px; line-height: 15px;
  }

  /* compliments slip */
  .slip { left: 48px; top: 705px; width: 792px; height: 373px; z-index: 2; }
  .slip .wordmark { left: 20px; top: 22px; gap: 10px; }
  .slip .mark-square { width: 74px; height: 74px; }
  .slip .name { font-size: 31px; }
  .slip .sub { font-size: 15px; }
  .slip .greeting { position: absolute; left: 30px; top: 333px; font-size: 20px; color: var(--brand-red); }

  /* business card back */
  .card-back {
    left: 395px; top: 443px; width: 525px; height: 302px; z-index: 3;
    background: radial-gradient(ellipse 360px 230px at 46% 30%, #c1262d 0%, #8a161c 40%, #3c0709 80%, #200304 100%);
  }
  .card-back .wordmark { left: 58px; top: 100px; gap: 18px; }
  .card-back .mark-square { width: 96px; height: 96px; }
  .card-back .name { font-size: 42px; }
  .card-back .sub { font-size: 20px; }

  /* business card front */
  .card-front { left: 298px; top: 222px; width: 522px; height: 301px; z-index: 4; }
  .card-front .wordmark { left: 15px; top: 110px; gap: 10px; }
  .card-front .mark-square { width: 46px; height: 46px; }
  .card-front .name { font-size: 24px; }
  .card-front .sub { font-size: 11.5px; }
  .card-front .details {
    position: absolute; right: 20px; top: 46px; text-align: right; color: var(--on-dark);
  }
  .card-front .person { font-size: 19px; letter-spacing: 0.3px; line-height: 24px; }
  .card-front .role { font-size: 15.5px; line-height: 20px; }
  .card-front .address { margin-top: 74px; font-size: 14px; line-height: 17.5px; }
  .card-front .contact { margin-top: 17px; font-size: 14px; line-height: 17.5px; }
  .card-front .registration {
    position: absolute; left: 15px; top: 262px; font-size: 9.5px; font-weight: bold;
    letter-spacing: 0.8px; line-height: 12.5px;
  }
</style>
</head>
<body>

  <section class="sheet letterhead" aria-label="Letterhead">
    <svg class="swoosh" viewBox="0 0 800 1133" preserveAspectRatio="none" aria-hidden="true">
      <defs>
        <linearGradient id="lh-band" x1="0" y1="1" x2="1" y2="0">
          <stop offset="0" stop-color="#1a0304"/>
          <stop offset="0.6" stop-color="#4a0a0e"/>
          <stop offset="1" stop-color="#7d1419"/>
        </linearGradient>
      </defs>
      <path d="M0,1133 L0,1125 C250,1090 560,1060 800,950 L800,1133 Z" fill="url(#lh-band)"/>
    </svg>
    <div class="wordmark">
      <span class="mark-square"></span>
      <span><span class="name">Keeping Steady</span><span class="sub">Paramedical Services Pty Ltd</span></span>
    </div>
    <div class="footer">
      47 Wattlebrook Drive, Fernhollow Vic 3091<br>
      P: 1800 462 817 E: enquiries@keepsteady.com.au&nbsp; W: www.keepsteady.com.au<br>
      ABN - 82 463 915 207 ACN - 264 871 035
    </div>
  </section>

  <section class="sheet slip" aria-label="With compliments slip">
    <svg class="swoosh" viewBox="0 0 792 373" preserveAspectRatio="none" aria-hidden="true">
      <defs>
        <radialGradient id="slip-band" cx="720" cy="80" r="300" gradientUnits="userSpaceOnUse">
          <stop offset="0" stop-color="#9e1d24"/>
          <stop offset="0.45" stop-color="#4a090d"/>
          <stop offset="1" stop-color="#0d0506"/>
        </radialGradient>
      </defs>
      <path d="M700,0 C640,120 705,260 552,373 L792,373 L792,0 Z" fill="url(#slip-band)"/>
    </svg>
    <div class="wordmark">
      <span class="mark-square"></span>
      <span><span class="name">Keeping Steady</span><span class="sub">Paramedical Services Pty Ltd</span></span>
    </div>
    <p class="greeting">With Compliments...</p>
  </section>

  <section class="sheet card-back" aria-label="Business card, back">
    <div class="wordmark on-dark">
      <span class="mark-square"></span>
      <span><span class="name">Keeping Steady</span><span class="sub">Paramedical Services Pty Ltd</span></span>
    </div>
  </section>

  <section class="sheet card-front" aria-label="Business card, front">
    <svg class="swoosh" viewBox="0 0 522 301" preserveAspectRatio="none" aria-hidden="true">
      <defs>
        <radialGradient id="card-band" cx="300" cy="110" r="260" gradientUnits="userSpaceOnUse">
          <stop offset="0" stop-color="#b3222a"/>
          <stop offset="0.45" stop-color="#5a0b10"/>
          <stop offset="1" stop-color="#0d0506"/>
        </radialGradient>
      </defs>
      <path d="M305,0 C270,90 305,210 212,301 L522,301 L522,0 Z" fill="url(#card-band)"/>
    </svg>
    <div class="wordmark">
      <span class="mark-square"></span>
      <span><span class="name">Keeping Steady</span><span class="sub">Paramedical Services Pty Ltd</span></span>
    </div>
    <div class="registration">ABN - 82 463 915 207<br>ACN - 264 871 035</div>
    <div class="details">
      <p class="person">Maree ‘Mo’ Calder</p>
      <p class="role">Field Care Coordinator</p>
      <p class="address">47 Wattlebrook Drive,<br>Fernhollow Vic 3091</p>
      <p class="contact">M: 0412 583 906<br>P: 1800 462 817<br>E: enquiries@keepsteady.com.au<br>W: www.keepsteady.com.au</p>
    </div>
  </section>

</body>
</html>
```